Its time for your mortgage check up

Complete Ad for Social Media Campaign

Target Market(s)

potential mortgage customers

Colors

Designer to choose colors to be used in the design.

Requirements
Must have
• Rates are dropping
• Its Time for your Mortgage Check Up
• Free Written Proposal Detailing Potential Benefits and Savings
• * Same Day Response
• * No Credit Check
• * No Fee or Obligation
• Contact us today at (800) 417-6290
• Harborlight Lending Group, Inc.
• 7200 Wexbury Lane, Larkfield, MD 21987
• NMLS #381746

```html
<!DOCTYPE html>
<html lang="en">
<head>
<meta charset="utf-8">
<title>Rates are dropping – Mortgage Check Up</title>
<link rel="stylesheet" href="https://fonts.googleapis.com/css2?family=Playfair+Display:wght@700&family=Oswald:wght@400;500&family=Roboto+Condensed:wght@400;500&display=swap">
<style>
  :root {
    --navy: #0f3a7a;
    --navy-deep: #0b2f66;
    --gold: #b8a46a;
    --white: #ffffff;
    --grass-dark: #2f5a12;
    --grass-mid: #5f9a1e;
    --grass-light: #8cc63a;
  }
  * { margin: 0; padding: 0; box-sizing: border-box; }
  html, body { width: 1200px; height: 1200px; overflow: hidden; background: var(--white); }
  .ad {
    position: relative;
    width: 1200px;
    height: 1200px;
    overflow: hidden;
    font-family: "Oswald", sans-serif;
    color: var(--white);
  }
  .header {
    position: absolute;
    left: 0; top: 0;
    width: 1200px; height: 232px;
    background: var(--navy);
  }
  .headline {
    position: absolute;
    left: 32px; top: 12px;
    font-family: "Playfair Display", serif;
    font-weight: 700;
    font-size: 84px;
    line-height: 1.1;
    white-space: nowrap;
  }
  .subhead {
    position: absolute;
    left: 63px; top: 134px;
    font-family: "Roboto Condensed", sans-serif;
    font-weight: 400;
    font-size: 40px;
    line-height: 1.1;
    white-space: nowrap;
  }
  .brand-panel {
    position: absolute;
    right: 0; top: 0;
    width: 360px; height: 232px;
    background: var(--white);
    border-radius: 170px 0 0 170px;
    display: flex;
    align-items: center;
    justify-content: center;
    gap: 14px;
    padding: 0 30px 0 50px;
  }
  .brand-mark {
    flex: none;
    width: 22px; height: 22px;
    background: var(--navy);
  }
  .brand-name {
    font-family: "Oswald", sans-serif;
    font-weight: 500;
    font-size: 30px;
    line-height: 1.15;
    color: var(--navy);
  }
  .hero-photo {
    position: absolute;
    left: 0; top: 232px;
    width: 1200px; height: 818px;
    background:
      radial-gradient(ellipse at 80% 80%, var(--grass-light) 0%, transparent 55%),
      linear-gradient(160deg, var(--grass-dark) 0%, var(--grass-mid) 45%, var(--grass-light) 100%);
  }
  .housing-badge {
    position: absolute;
    left: 1000px; top: 285px;
    width: 86px; height: 136px;
  }
  .offer {
    position: absolute;
    left: 113px; top: 336px;
    font-family: "Oswald", sans-serif;
    font-weight: 500;
    font-size: 61px;
    line-height: 64px;
    white-space: nowrap;
  }
  .benefits {
    position: absolute;
    left: 108px; top: 610px;
    list-style: none;
  }
  .benefit {
    display: flex;
    align-items: center;
    width: 447px; height: 60px;
    margin-bottom: 15px;
    padding-left: 30px;
    background: var(--navy);
    font-family: "Oswald", sans-serif;
    font-weight: 500;
    font-size: 42px;
    white-space: nowrap;
  }
  .benefit::before {
    content: "";
    flex: none;
    width: 24px; height: 24px;
    margin-right: 28px;
    background: var(--gold);
  }
  .footer {
    position: absolute;
    left: 0; top: 1050px;
    width: 1200px; height: 150px;
    background: var(--navy-deep);
  }
  .contact-line {
    position: absolute;
    left: 28px; top: 6px;
    font-family: "Playfair Display", serif;
    font-weight: 700;
    font-size: 71px;
    line-height: 1.2;
    white-space: nowrap;
  }
  .company-info {
    position: absolute;
    top: 98px;
    font-family: "Roboto Condensed", sans-serif;
    font-weight: 500;
    font-size: 26px;
    white-space: nowrap;
  }
  .company-name { left: 28px; }
  .company-address { left: 420px; }
  .company-license { right: 57px; }
</style>
</head>
<body>
<div class="ad">
  <header class="header">
    <h1 class="headline">Rates are dropping</h1>
    <p class="subhead">ITS TIME FOR YOUR MORTGAGE CHECK UP</p>
    <div class="brand-panel">
      <span class="brand-mark"></span>
      <span class="brand-name">Harborlight Lending Group, Inc.</span>
    </div>
  </header>

  <div class="hero-photo" role="img" aria-label="Photo of a small wooden toy house standing on bright green grass"></div>

  <svg class="housing-badge" viewBox="0 0 86 136" aria-hidden="true">
    <rect x="0" y="0" width="86" height="136" fill="#ffffff"/>
  </svg>

  <p class="offer">Free Written Proposal<br>Detailing Potential Benefits<br>and Savings</p>

  <ul class="benefits">
    <li class="benefit">Same Day Response</li>
    <li class="benefit">No Credit Check</li>
    <li class="benefit">No Fee or Obligation</li>
  </ul>

  <footer class="footer">
    <p class="contact-line">Contact us today at (800) 417-6290</p>
    <span class="company-info company-name">Harborlight Lending Group, Inc.</span>
    <span class="company-info company-address">7200 Wexbury Lane, Larkfield, MD 21987</span>
    <span class="company-info company-license">NMLS #381746</span>
  </footer>
</div>
</body>
</html>
```